Label for wiphe fruit jam

We need a label design for a new, unique product.
It is a fruit jam. It is our invention.
We need an etiquette/label design for our new product ZelvoPuli. It is whiping fruits jam in transparent cup. We will have 3 sorts: mango in bright orange colour, strawberry in bright red colour and wild berries in violet
This fruit jam can be wipping with the mixer.
The overrun is up to 100%.
We need a design for this original product.
We have 3 products: mango, strawberry, wild berries.
We are looking for a fruity design. With strong colors. The design must be such that you want to eat the same product.
The product is for wipped desserts, fruity ice cream, pies.
Whipe it at home with simple kitchen mixer.
The size of the label on the side are: 100x55mm.
On top is round, diameter 80mm
Updates

The size of the label are: 100x55mm.On top is round, diameter 80mm Added Monday, February 13, 2017

Target Market(s)

Private customers, housewives, people who like to cook, make dessert, children who like to make ice themselves, etc.

Industry/Entity Type

Product

Requirements
Must have
• The name of the product is Zelvo Puli.
• Maybe you have a better name for this product?

```html
<!DOCTYPE html>
<html lang="en">
<head>
<meta charset="utf-8">
<title>ZelvoPuli Sweet Natural Jam – Labels</title>
<link rel="stylesheet" href="https://fonts.googleapis.com/css2?family=Oswald:wght@500;700&display=swap">
<style>
  :root {
    --page: #ececec;
    --label: #ffffff;
    --brand: #4a5fa8;
    --strawberry: #c42a2a;
    --strawberry-deep: #e0463f;
    --strawberry-soft: #f6c9c2;
    --mango: #e2672a;
    --mango-deep: #f29a3c;
    --mango-soft: #fbe0a8;
    --berry: #5a2b86;
    --berry-deep: #4b2f7e;
    --berry-soft: #d9cdea;
    --leaf: #6fb43a;
    --jam-tag: #f0941e;
  }
  * { margin: 0; padding: 0; box-sizing: border-box; }
  html, body { width: 753px; height: 1200px; overflow: hidden; }
  body {
    background: var(--page);
    font-family: "Oswald", sans-serif;
    display: flex;
    flex-direction: column;
    align-items: center;
    justify-content: center;
    gap: 48px;
  }
  .label {
    position: relative;
    width: 680px;
    height: 300px;
  }
  .label-shape { position: absolute; inset: 0; }
  .label-content {
    position: absolute;
    left: 190px;
    width: 300px;
    top: 34px;
    bottom: 22px;
    display: flex;
    flex-direction: column;
    align-items: center;
    justify-content: space-between;
    text-align: center;
  }
  .brand-name {
    font-weight: 500;
    font-size: 38px;
    line-height: 48px;
    color: var(--brand);
    letter-spacing: 1px;
    display: flex;
    align-items: center;
    gap: 10px;
  }
  .brand-dot {
    width: 16px; height: 16px;
    border-radius: 50%;
    background: var(--leaf);
  }
  .flavour {
    font-weight: 700;
    font-size: 42px;
    line-height: 52px;
    letter-spacing: 1px;
  }
  .label--strawberry .flavour { color: var(--strawberry); }
  .label--mango .flavour { color: var(--mango); }
  .label--berry .flavour { color: var(--berry); }
  .sweet-tag {
    padding: 0 18px;
    border: 3px solid var(--leaf);
    border-radius: 14px 2px 14px 2px;
    color: var(--leaf);
    font-weight: 700;
    font-size: 26px;
    line-height: 34px;
    letter-spacing: 2px;
  }
  .jam-tag {
    padding: 0 22px;
    background: var(--jam-tag);
    border-radius: 16px;
    color: #fff;
    font-weight: 700;
    font-size: 18px;
    line-height: 32px;
    letter-spacing: 3px;
  }
</style>
</head>
<body>

  <section class="label label--strawberry">
    <svg class="label-shape" viewBox="0 0 680 300" width="680" height="300">
      <defs>
        <radialGradient id="fruit-strawberry" cx="0.5" cy="0.5" r="0.7">
          <stop offset="0" stop-color="var(--strawberry-soft)"/>
          <stop offset="1" stop-color="var(--strawberry-deep)"/>
        </radialGradient>
      </defs>
      <rect x="0" y="50" width="680" height="250" fill="url(#fruit-strawberry)" role="img" aria-label="Scattered illustrated strawberries with leaves on white"/>
      <path d="M190 300 V150 A150 150 0 0 1 490 150 V300 Z" fill="var(--label)"/>
    </svg>
    <div class="label-content">
      <div class="brand-name"><span class="brand-dot"></span>ZelvoPuli</div>
      <div class="flavour">STRAWBERRIES</div>
      <div class="sweet-tag">SWEET</div>
      <div class="jam-tag">NATURAL JAM</div>
    </div>
  </section>

  <section class="label label--mango">
    <svg class="label-shape" viewBox="0 0 680 300" width="680" height="300">
      <defs>
        <radialGradient id="fruit-mango" cx="0.5" cy="0.5" r="0.7">
          <stop offset="0" stop-color="var(--mango-soft)"/>
          <stop offset="1" stop-color="var(--mango-deep)"/>
        </radialGradient>
      </defs>
      <rect x="0" y="50" width="680" height="250" fill="url(#fruit-mango)" role="img" aria-label="Scattered illustrated mangoes and mango slices on white"/>
      <path d="M190 300 V150 A150 150 0 0 1 490 150 V300 Z" fill="var(--label)"/>
    </svg>
    <div class="label-content">
      <div class="brand-name"><span class="brand-dot"></span>ZelvoPuli</div>
      <div class="flavour">MANGO</div>
      <div class="sweet-tag">SWEET</div>
      <div class="jam-tag">NATURAL JAM</div>
    </div>
  </section>

  <section class="label label--berry">
    <svg class="label-shape" viewBox="0 0 680 300" width="680" height="300">
      <defs>
        <radialGradient id="fruit-berry" cx="0.5" cy="0.5" r="0.7">
          <stop offset="0" stop-color="var(--berry-soft)"/>
          <stop offset="1" stop-color="var(--berry-deep)"/>
        </radialGradient>
      </defs>
      <rect x="0" y="50" width="680" height="250" fill="url(#fruit-berry)" role="img" aria-label="Scattered illustrated blackberries with leaves on white"/>
      <path d="M190 300 V150 A150 150 0 0 1 490 150 V300 Z" fill="var(--label)"/>
    </svg>
    <div class="label-content">
      <div class="brand-name"><span class="brand-dot"></span>ZelvoPuli</div>
      <div class="flavour">WILD BERRIES</div>
      <div class="sweet-tag">SWEET</div>
      <div class="jam-tag">NATURAL JAM</div>
    </div>
  </section>

</body>
</html>
```